We are starting a new service that will combine local city menus and specials from local restaurants that will then be emailed and printed out on our website.. its a free service to the subscribers and a small charge to the restaurants. We need something to reflect the restaurant industry and to appeal to the general public alike, free to the end user. They sign up and receive daily specials in an email from our site.. not just one city but any one they pick that we service.. We would need links to include. Home, About Us, Sign Up (for free to public), Add Your Restaurant (increase sales and reduce daily calls).. and Contact Us link.. the name of the service is Town Plates in Motion and website will be townplatesinmotion.example. thank you

```html
<!DOCTYPE html>
<html lang="en">
<head>
<meta charset="utf-8">
<title>Town Plates in Motion</title>
<link rel="stylesheet" href="https://fonts.googleapis.com/css2?family=Noto+Sans:wght@400;700&display=swap">
<style>
:root{
  --ink:#333333;
  --muted:#555555;
  --link:#428bca;
  --accent:#5bc0de;
  --nav-bg:#222222;
  --nav-active:#080808;
  --nav-text:#9d9d9d;
  --line:#e5e5e5;
  --field-border:#cccccc;
  --page:#ffffff;
}
*{box-sizing:border-box;margin:0;padding:0}
html,body{width:1200px;height:1200px;overflow:hidden;background:var(--page)}
body{font-family:"Noto Sans",sans-serif;color:var(--ink);position:relative}
.abs{position:absolute}

/* brand strip */
.brand-strip{left:14px;top:10px;height:40px;display:flex;align-items:center;gap:6px;font-size:13px;font-weight:700;color:var(--ink)}
.brand-strip .dot{width:18px;height:18px;border-radius:50%;background:#b22222}

/* navbar */
.navbar{left:0;top:58px;width:1200px;height:38px;background:var(--nav-bg);border-bottom:1px solid #080808}
.navbar .site-name{left:48px;top:0;line-height:38px;font-size:15px;letter-spacing:.5px;color:var(--nav-text)}
.nav-links{left:466px;top:0;display:flex;height:38px}
.nav-links a{display:block;line-height:38px;padding:0 18px;font-size:12px;color:var(--nav-text);text-decoration:none}
.nav-links a.active{background:var(--nav-active);color:#fff;font-weight:700;width:78px;text-align:center;padding:0}
.caret{display:inline-block;width:0;height:0;border-left:4px solid transparent;border-right:4px solid transparent;border-top:4px solid var(--nav-text);vertical-align:middle;margin-left:4px}
.search{left:796px;top:5px;width:258px;height:27px;background:#fff;border-radius:3px;font-size:12px;color:#777;padding:5px 14px}
.nav-submit{left:1066px;top:5px;width:84px;height:27px;background:#fff;border-radius:3px;font-size:13px;font-weight:700;text-align:center;line-height:27px;color:var(--ink)}

/* hero */
.hero{left:48px;top:110px;width:1102px;height:261px;background:linear-gradient(180deg,#c9a27a 0%,#5a3f2c 28%,#1d1b1e 55%,#121215 100%)}
.hero .arrow{top:112px}
.hero .dots{left:526px;top:226px;display:flex;gap:5px}
.hero .dots span{width:11px;height:11px;border-radius:50%;border:1px solid #fff}
.hero .dots span.on{background:#fff}

/* sign up */
.signup{left:48px;top:430px;width:250px;text-align:center}
.signup h2{font-size:19px;font-weight:400;line-height:19px;color:#222}
.signup p{margin-top:12px;font-size:11px;line-height:12.5px;text-align:justify;text-align-last:left}
.field{height:26px;border:1px solid var(--field-border);border-radius:3px;font-size:13px;color:#888;padding:3px 14px;text-align:left;background:#fff}
.signup .field{width:250px}
.btn-blue{height:26px;background:var(--accent);border-radius:3px;color:#fff;font-size:13px;text-align:center;line-height:26px}
.terms{font-size:12px;line-height:16px;color:var(--ink)}
.terms a,.link{color:var(--link);text-decoration:none}

/* feature columns */
.feature{width:252px;text-align:center}
.feature .thumb{width:58px;height:58px;margin:0 auto}
.feature h3{margin-top:9px;font-size:10.5px;font-weight:400;color:var(--link);letter-spacing:.3px}
.feature p{margin-top:5px;font-size:11px;line-height:12.8px;letter-spacing:.2px;text-align:justify;text-align-last:left}
.btn-outline{display:inline-block;margin-top:10px;width:114px;height:26px;border:1px solid var(--field-border);border-radius:3px;font-size:13px;line-height:24px;color:var(--ink)}

.rule{left:48px;width:1102px;height:1px;background:var(--line)}

/* add restaurant */
.add-title{left:0;width:1200px;top:826px;text-align:center;font-size:19px;color:var(--link);letter-spacing:.5px}
.pitch{left:137px;top:860px;width:445px}
.pitch h4{font-size:16px;font-weight:400;color:var(--link);letter-spacing:.4px;line-height:20px}
.pitch p{margin:4px 0 11px;font-size:14px;line-height:15.6px;letter-spacing:.4px;text-align:justify;text-align-last:left;color:#222}
.add-form{left:618px;top:856px;width:444px}
.add-form .field{margin-bottom:10px}
.add-form .btn-blue{font-weight:700;font-size:12px;height:25px;line-height:25px}

/* footer */
.footer-col{top:1078px;font-size:11px;color:#222;line-height:13.5px}
.footer-col h5{font-size:11px;font-weight:400;margin-bottom:7px;letter-spacing:.3px}
.footer-col ul{padding-left:48px}
.footer-col ul.social{padding-left:16px;list-style:disc}
.social li{line-height:24px}
.social .mark{display:inline-block;width:18px;height:18px;background:#111;border-radius:3px;vertical-align:middle;margin-right:2px}
.copyright{left:0;width:1200px;top:1177px;text-align:center;font-size:12px;color:#222}
</style>
</head>
<body>

<div class="abs brand-strip"><span class="dot"></span>Town Plates</div>

<nav class="abs navbar">
  <div class="abs site-name">TOWN PLATES in MOTION</div>
  <div class="abs nav-links">
    <a class="active" href="#">Home</a>
    <a href="#">About Us <span class="caret"></span></a>
    <a href="#">Contact Us</a>
  </div>
  <div class="abs search">Search</div>
  <div class="abs nav-submit">Submit</div>
</nav>

<section class="abs hero" role="img" aria-label="Close-up photo of a dark leather restaurant menu with gold lettering on a dining table">
  <svg class="abs arrow" style="left:70px" width="26" height="30" viewBox="0 0 26 30"><path d="M20 3 L6 15 L20 27" fill="none" stroke="#fff" stroke-opacity=".8" stroke-width="5"/></svg>
  <svg class="abs arrow" style="left:1006px" width="26" height="30" viewBox="0 0 26 30"><path d="M6 3 L20 15 L6 27" fill="none" stroke="#fff" stroke-opacity=".8" stroke-width="5"/></svg>
  <div class="abs dots"><span class="on"></span><span></span><span></span></div>
</section>

<section class="abs signup">
  <h2>Sign Up with TOWN<br>PLATES</h2>
  <p>Lorem Ipsum is simply dummy text of the printing and typesetting industry. Lorem Ipsum has been the industry's standard dummy text ever since the 1500s, when an unknown printer took a galley of type and scrambled it to make a type specimen book.</p>
  <div class="field" style="margin-top:8px">Your E-mail</div>
  <div class="field" style="margin-top:10px">Password</div>
  <div class="field">Confirmation</div>
  <div class="btn-blue" style="margin-top:10px">Sign Up</div>
  <p class="terms" style="margin-top:10px;text-align:center;text-align-last:center">By signing up you agree to <a href="#">Terms of Use</a> and <a href="#">Privacy Policy</a></p>
</section>

<article class="abs feature" style="left:332px;top:418px">
  <div class="thumb" role="img" aria-label="Photo of a grilled steak plate" style="background:linear-gradient(135deg,#d98b3a,#6b3414)"></div>
  <h3>DAILY SPECIAL</h3>
  <p>Lorem Ipsum is simply dummy text of the printing and typesetting industry. Lorem Ipsum has been the industry's standard dummy text ever since the 1500s, when an unknown printer took a galley of type and scrambled it to make a type specimen book. It has survived not only five centuries, but also the leap into electronic typesetting, remaining essentially unchanged.</p>
  <span class="btn-outline">Read More</span>
</article>

<article class="abs feature" style="left:616px;top:418px">
  <div class="thumb" role="img" aria-label="Printed restaurant menu page" style="background:linear-gradient(180deg,#d8d8d8,#f4f4f4)"></div>
  <h3>MENU COMBO</h3>
  <p>Lorem Ipsum is simply dummy text of the printing and typesetting industry. Lorem Ipsum has been the industry's standard dummy text ever since the 1500s, when an unknown printer took a galley of type and scrambled it to make a type specimen book. It has survived not only five centuries, but also the leap into electronic typesetting, remaining essentially unchanged.</p>
  <span class="btn-outline">Read More</span>
</article>

<article class="abs feature" style="left:900px;top:418px">
  <div class="thumb" role="img" aria-label="City skyline at dusk" style="background:linear-gradient(180deg,#3b4f86,#c46a2e)"></div>
  <h3>LOCATE A RESTAURANT</h3>
  <p>Lorem Ipsum is simply dummy text of the printing and typesetting industry. Lorem Ipsum has been the industry's standard dummy text ever since the 1500s, when an unknown printer took a galley of type and scrambled it to make a type specimen book. It has survived not only five centuries, but also the leap into electronic typesetting, remaining essentially unchanged.</p>
  <span class="btn-outline">Read More</span>
</article>

<div class="abs rule" style="top:764px"></div>

<h2 class="abs add-title" style="font-weight:400">Add You Restaurant</h2>

<section class="abs pitch">
  <h4>Increase Sales</h4>
  <p>Lorem Ipsum has been the industry's standard dummy text ever since the 1500s, when an unknown printer took a galley of type and scrambled it to make a type specimen book.</p>
  <h4>Reduce Daily Calls</h4>
  <p>Lorem Ipsum has been the industry's standard dummy text ever since the 1500s, when an unknown printer took a galley of type and scrambled it to make a type specimen book.</p>
</section>

<form class="abs add-form">
  <div class="field">Restaurant Name</div>
  <div class="field">Location</div>
  <div class="field">Lorem Ipsum</div>
  <div class="field">Lorem Ipsum</div>
  <div class="btn-blue">Submit</div>
</form>

<div class="abs rule" style="top:1059px"></div>

<footer>
  <div class="abs footer-col" style="left:67px">
    <h5>FIND A RESTAURANT</h5>
    <ul><li>Europe</li><li>N. America</li><li>Asia</li><li>Australia</li><li>S. America</li></ul>
  </div>
  <div class="abs footer-col" style="left:342px">
    <h5>ABOUT US</h5>
    <ul><li>Our Blog</li><li>Recipés</li><li>Plates in Motion</li></ul>
  </div>
  <div class="abs footer-col" style="left:618px">
    <h5>ALL MENUS</h5>
    <ul><li>Today's Specials</li><li>Lorem Ipsum</li></ul>
  </div>
  <div class="abs footer-col" style="left:894px">
    <h5>CONNECT WITH US</h5>
    <ul class="social">
      <li><span class="mark"></span><span class="link">Friendpage</span></li>
      <li><span class="mark"></span><span class="link">Talk</span></li>
      <li><span class="mark"></span><span class="link">Chirpline</span></li>
    </ul>
  </div>
  <div class="abs copyright">Copyright © Town Plates in Motion 2014</div>
</footer>

</body>
</html>
```